Saffron Ledger Works Flyer

We need a one page promotional piece that explains what our company does, and the benefits it provides in a simple, elegant, easy to understand way. I would like to print it on glossy heavyweight paper to give a feel of high quality and legitimacy. I will include the logo, the tag line, and the main benefits that the company offers.

Tag line concept, may not need these exact words. "Give us 5 minutes a day, and we will help you build a Saffron Ledger Works."

Key points...(exact wording not required if you think of a better way to say it)

Software easy enough for my grandpa to use.
Lets you use snail mail, email, texting, and social media to quickly market to your customers at very low cost.
Web based which allows you to launch media campaigns from your desktop, or smartphone in moments.
Quick 3 - 5 minute training videos which give you hard hitting, quick action tips that will help you make your business better today.
Live coaching calls to help motivate you to improve your business.
No contracts, or start up fees. One low price of $299 per month.

Restaurant owners

Restaurant

```html
<!DOCTYPE html>
<html lang="en">
<head>
<meta charset="utf-8">
<title>Saffron Ledger Works Flyer</title>
<link rel="stylesheet" href="https://fonts.googleapis.com/css2?family=Arimo:wght@700&family=Fira+Sans+Condensed:wght@400;700&display=swap">
<style>
  :root {
    --backdrop: #e8e5e0;
    --sheet-top: #e6eef5;
    --brand-blue: #1b5aa6;
    --band-red: #e02a2c;
    --band-red-light: #ef4a48;
    --badge-green: #3f9a3c;
    --panel-blue: #a9c9eb;
    --rule-blue: #3d7fc6;
    --ink: #111111;
    --white: #ffffff;
    --tick-green: #4b9b2e;
    --logo-ink: #555555;
  }
  * { box-sizing: border-box; margin: 0; padding: 0; }
  html, body { width: 922px; height: 1200px; overflow: hidden; }
  body { background: var(--backdrop); position: relative; }

  .flyer {
    position: absolute; left: 39px; top: 0;
    width: 844px; height: 1200px;
    background: var(--panel-blue);
    overflow: hidden;
  }
  .masthead {
    position: absolute; left: 0; top: 0; width: 100%; height: 140px;
    background: linear-gradient(180deg, #f3f7fa 0%, var(--sheet-top) 100%);
  }
  .masthead__name {
    position: absolute; left: 0; right: 0; top: 44px;
    text-align: center;
    font-family: "Arimo", Arial, sans-serif; font-weight: 700;
    font-size: 60px; letter-spacing: -0.5px;
    color: var(--brand-blue); text-transform: uppercase;
    transform: scaleY(1.08);
  }
  .hero-band {
    position: absolute; left: 0; top: 140px; width: 100%; height: 335px;
    background: linear-gradient(90deg, var(--band-red) 0%, var(--band-red) 80%, var(--band-red-light) 100%);
  }
  .hero-band__tab {
    position: absolute; left: 245px; top: 140px; width: 354px; height: 22px;
    background: var(--sheet-top);
    border-radius: 0 0 14px 14px;
  }
  .badge {
    position: absolute; left: 273px; top: 168px; width: 298px; height: 52px;
    background: linear-gradient(180deg, #55b04e 0%, var(--badge-green) 100%);
    border: 2px solid #e9f3e6; border-radius: 4px;
    color: var(--white);
    font-family: "Fira Sans Condensed", "Arial Narrow", sans-serif; font-weight: 700;
    font-size: 31px; line-height: 48px; text-align: center; text-transform: uppercase;
  }
  .tagline {
    position: absolute; left: 40px; right: 40px; top: 235px;
    text-align: center; color: var(--white);
    font-family: "Fira Sans Condensed", "Arial Narrow", sans-serif; font-weight: 700;
    font-size: 56px; line-height: 68px;
  }
  .hero-band__foot {
    position: absolute; left: 560px; top: 462px; width: 284px; height: 13px;
    background: var(--band-red-light);
    border-radius: 10px 0 0 0;
  }

  .benefits {
    position: absolute; left: 48px; top: 492px; width: 750px;
    font-family: "Fira Sans Condensed", "Arial Narrow", sans-serif; color: var(--ink);
  }
  .benefits__lead { font-weight: 700; font-size: 31px; line-height: 40px; margin-bottom: 14px; }
  .benefit-list { list-style: none; }
  .benefit {
    position: relative; padding: 6px 0 9px 37px;
    font-size: 22px; line-height: 29px;
    border-bottom: 2px solid var(--rule-blue);
    margin-bottom: 8px;
  }
  .benefit:last-child { border-bottom: none; }
  .benefit__tick { position: absolute; left: 0; top: 9px; width: 28px; height: 28px; }

  .brand-mark {
    position: absolute; left: 0; right: 0; top: 1075px;
    display: flex; align-items: center; justify-content: center; gap: 16px;
  }
  .brand-mark__dot { width: 26px; height: 26px; border-radius: 50%; background: var(--logo-ink); }
  .brand-mark__name {
    font-family: "Fira Sans Condensed", "Arial Narrow", sans-serif; font-weight: 700;
    font-size: 46px; color: var(--logo-ink);
  }
</style>
</head>
<body>
<main class="flyer">
  <header class="masthead">
    <h1 class="masthead__name">Saffron Ledger Works</h1>
  </header>
  <section class="hero-band" aria-hidden="true"></section>
  <div class="hero-band__tab" aria-hidden="true"></div>
  <div class="hero-band__foot" aria-hidden="true"></div>
  <div class="badge">Easy Use Machine</div>
  <p class="tagline">Give us 5 minutes a day, and we will help you build a Saffron Ledger Works.</p>

  <section class="benefits">
    <h2 class="benefits__lead">Software easy enough for my grandpa to use.</h2>
    <ul class="benefit-list">
      <li class="benefit">
        <svg class="benefit__tick" viewBox="0 0 28 28"><circle cx="14" cy="14" r="13" fill="#4b9b2e" stroke="#2f6f1c" stroke-width="1.5"/><path d="M7.5 14.5l4.5 4.5 9-10" fill="none" stroke="#fff" stroke-width="3.2" stroke-linecap="round" stroke-linejoin="round"/></svg>
        Lets you use snail mail, email, texting, and social media to quickly market to your customers at very low cost.
      </li>
      <li class="benefit">
        <svg class="benefit__tick" viewBox="0 0 28 28"><circle cx="14" cy="14" r="13" fill="#4b9b2e" stroke="#2f6f1c" stroke-width="1.5"/><path d="M7.5 14.5l4.5 4.5 9-10" fill="none" stroke="#fff" stroke-width="3.2" stroke-linecap="round" stroke-linejoin="round"/></svg>
        Web based which allows you to launch media campaigns from your desktop, or smartphone in moments.
      </li>
      <li class="benefit">
        <svg class="benefit__tick" viewBox="0 0 28 28"><circle cx="14" cy="14" r="13" fill="#4b9b2e" stroke="#2f6f1c" stroke-width="1.5"/><path d="M7.5 14.5l4.5 4.5 9-10" fill="none" stroke="#fff" stroke-width="3.2" stroke-linecap="round" stroke-linejoin="round"/></svg>
        Quick 3 - 5 minute training videos which give you hard hitting, quick action tips that will help you make your business better today.
      </li>
      <li class="benefit">
        <svg class="benefit__tick" viewBox="0 0 28 28"><circle cx="14" cy="14" r="13" fill="#4b9b2e" stroke="#2f6f1c" stroke-width="1.5"/><path d="M7.5 14.5l4.5 4.5 9-10" fill="none" stroke="#fff" stroke-width="3.2" stroke-linecap="round" stroke-linejoin="round"/></svg>
        Live coaching calls to help motivate you to improve your business
      </li>
      <li class="benefit">
        <svg class="benefit__tick" viewBox="0 0 28 28"><circle cx="14" cy="14" r="13" fill="#4b9b2e" stroke="#2f6f1c" stroke-width="1.5"/><path d="M7.5 14.5l4.5 4.5 9-10" fill="none" stroke="#fff" stroke-width="3.2" stroke-linecap="round" stroke-linejoin="round"/></svg>
        No contracts, or start up fees. One low price of $299 per month.
      </li>
    </ul>
  </section>

  <footer class="brand-mark">
    <span class="brand-mark__dot" aria-hidden="true"></span>
    <span class="brand-mark__name">Saffron Ledger Works</span>
  </footer>
</main>
</body>
</html>
```